Need business card designed for a Mobile RV Repair business

I need a business card designed

Welding sparks

Industry/Entity Type

Rv Repair , Mobile Welding & Fabrication

Contact Information for Business Card

Colors
0054AA
0677BA
7BADD7
CADEEF
E8F1F8

Requirements
Nice to have
• welding sparks, list of services, welding vector

```html
<!DOCTYPE html>
<html lang="en">
<head>
<meta charset="utf-8">
<title>Ridgeline Mobile RV &amp; Motorhome Repair — Business Card</title>
<link rel="stylesheet" href="https://fonts.googleapis.com/css2?family=Roboto:wght@400;500;700&display=swap">
<style>
  :root {
    --teal: #0f8a80;
    --teal-dark: #0b7169;
    --orange: #f19a0c;
    --yellow: #f4e21a;
    --ink: #2b2b2b;
    --paper: #ffffff;
    --stage: #e9ecef;
    --photo-a: #8d9399;
    --photo-b: #a7adb2;
    --photo-c: #7f8a90;
  }
  * { box-sizing: border-box; margin: 0; padding: 0; }
  html, body { width: 1200px; height: 900px; overflow: hidden; }
  body {
    background: var(--stage);
    font-family: "Roboto", Arial, sans-serif;
    color: var(--ink);
    position: relative;
  }
  .card {
    position: absolute;
    width: 640px;
    height: 380px;
    background: var(--paper);
    overflow: hidden;
    box-shadow: 0 8px 24px rgba(0,0,0,.18);
  }
  /* ---------- services side ---------- */
  .card--services { left: 80px; top: 46px; }
  .work-photo {
    position: absolute; top: 0; height: 100%;
  }
  .work-photo--interior {
    left: 0; width: 190px;
    background: linear-gradient(160deg, #c9cdd0, var(--photo-a));
    clip-path: polygon(20px 0, 100% 0, 78% 100%, 0 100%, 0 35px);
  }
  .work-photo--frames {
    left: 150px; width: 170px;
    background: linear-gradient(170deg, #d4d6d8, var(--photo-b) 55%, #6c7378);
    clip-path: polygon(38% 0, 100% 0, 100% 100%, 4% 100%);
  }
  .work-photo--trailer {
    left: 318px; top: 212px; height: 168px; width: 104px;
    background: linear-gradient(180deg, #b9c8d3, var(--photo-c));
    clip-path: polygon(0 0, 100% 6%, 100% 100%, 0 100%);
  }
  .services {
    position: absolute; right: 28px; top: 22px;
    text-align: right;
  }
  .services__title {
    font-size: 22px; font-weight: 700; color: var(--teal);
    margin-bottom: 6px; margin-right: 22px;
  }
  .services__list { list-style: none; }
  .services__item {
    font-size: 14px; line-height: 20px; color: var(--ink);
    display: flex; justify-content: flex-end; align-items: center; gap: 8px;
  }
  .services__item svg { width: 12px; height: 12px; flex: none; }
  .brand-mark {
    position: absolute; display: flex; align-items: center; gap: 8px;
    font-weight: 700; color: var(--ink); text-transform: uppercase;
  }
  .brand-mark__dot { border-radius: 50%; background: var(--teal); flex: none; }
  .card--services .brand-mark {
    right: 28px; bottom: 26px; font-size: 12px; line-height: 16px;
    width: 186px;
  }
  .card--services .brand-mark__dot { width: 14px; height: 14px; }

  /* ---------- contact side ---------- */
  .card--contact { left: 480px; top: 474px; }
  .card--contact .brand-mark { left: 34px; top: 90px; font-size: 15px; }
  .card--contact .brand-mark__dot { width: 18px; height: 18px; }
  .wave { position: absolute; inset: 0; }
  .contact {
    position: absolute; left: 40px; bottom: 30px; color: #fff;
  }
  .contact__name {
    font-size: 22px; font-weight: 700; color: var(--yellow);
    text-transform: uppercase; letter-spacing: .3px;
  }
  .contact__role { font-weight: 400; color: #fff; font-size: 19px; text-transform: none; }
  .contact__line {
    margin-top: 8px; font-size: 15px; display: flex; align-items: center; gap: 8px;
  }
  .contact__line svg { width: 15px; height: 15px; flex: none; }
  .contact__sep { opacity: .9; }
</style>
</head>
<body>

<section class="card card--services" aria-label="Services side">
  <div class="work-photo work-photo--interior" role="img" aria-label="Photo of a finished trailer interior"></div>
  <div class="work-photo work-photo--frames" role="img" aria-label="Photo of welded steel frames in a workshop"></div>
  <div class="work-photo work-photo--trailer" role="img" aria-label="Photo of a trailer structure under fabrication"></div>

  <div class="services">
    <h2 class="services__title">Our Services</h2>
    <ul class="services__list">
      <li class="services__item">Mobile Welding <svg viewBox="0 0 12 12"><path d="M1 10 L11 6 L1 2 L4 6 Z" fill="var(--teal)"/></svg></li>
      <li class="services__item">Steel | Stainless Steel | Aluminum <svg viewBox="0 0 12 12"><path d="M1 10 L11 6 L1 2 L4 6 Z" fill="var(--teal)"/></svg></li>
      <li class="services__item">Custom Fences, Gates <svg viewBox="0 0 12 12"><path d="M1 10 L11 6 L1 2 L4 6 Z" fill="var(--teal)"/></svg></li>
      <li class="services__item">Custom Fabrication Work <svg viewBox="0 0 12 12"><path d="M1 10 L11 6 L1 2 L4 6 Z" fill="var(--teal)"/></svg></li>
      <li class="services__item">Repairs to Existing Structures <svg viewBox="0 0 12 12"><path d="M1 10 L11 6 L1 2 L4 6 Z" fill="var(--teal)"/></svg></li>
      <li class="services__item">RV and Motorhome Repairs <svg viewBox="0 0 12 12"><path d="M1 10 L11 6 L1 2 L4 6 Z" fill="var(--teal)"/></svg></li>
      <li class="services__item">Electrical, Plumbing &amp; more! <svg viewBox="0 0 12 12"><path d="M1 10 L11 6 L1 2 L4 6 Z" fill="var(--teal)"/></svg></li>
    </ul>
  </div>

  <div class="brand-mark"><span class="brand-mark__dot"></span><span>Ridgeline Mobile RV &amp; Motorhome Repair</span></div>
</section>

<section class="card card--contact" aria-label="Contact side">
  <svg class="wave" viewBox="0 0 640 380" preserveAspectRatio="none" aria-hidden="true">
    <defs>
      <linearGradient id="edge" x1="0" x2="1" y1="0" y2="0">
        <stop offset="0" stop-color="var(--orange)"/>
        <stop offset=".55" stop-color="var(--yellow)"/>
        <stop offset="1" stop-color="var(--orange)"/>
      </linearGradient>
      <linearGradient id="band" x1="0" x2="1" y1="1" y2="0">
        <stop offset="0" stop-color="var(--teal)"/>
        <stop offset="1" stop-color="var(--teal-dark)"/>
      </linearGradient>
    </defs>
    <path d="M0,380 L0,300 C40,225 120,200 260,208 C420,218 560,190 640,60 L640,380 Z" fill="url(#band)"/>
    <path d="M0,300 C40,225 120,200 260,208 C420,218 560,190 640,60" fill="none" stroke="url(#edge)" stroke-width="6"/>
  </svg>

  <div class="brand-mark"><span class="brand-mark__dot"></span>Ridgeline Mobile RV &amp; Motorhome Repair</div>

  <div class="contact">
    <p class="contact__name">Marco Ellison <span class="contact__role">| Owner</span></p>
    <p class="contact__line">
      <svg viewBox="0 0 16 16"><path d="M3 1.5 L6 1.5 L7 5 L5 6.3 C6 8.5 7.5 10 9.7 11 L11 9 L14.5 10 L14.5 13 C14.5 14 13.5 14.6 12.5 14.5 C6.5 14 2 9.5 1.5 3.5 C1.4 2.5 2 1.5 3 1.5 Z" fill="var(--yellow)"/></svg>
      555.014.2290 <span class="contact__sep">|</span>
      <svg viewBox="0 0 16 16"><rect x="1" y="3" width="14" height="10" rx="1.5" fill="var(--yellow)"/><path d="M1.5 4 L8 9 L14.5 4" fill="none" stroke="var(--teal)" stroke-width="1.4"/></svg>
      ridgelinerv@example.com
    </p>
  </div>
</section>

</body>
</html>
```